Cosmetic Dentist Practice needs stationery package/logo

I need a letterhead, envelope and business card for a cosmetic and Dental Inplant practice in an upscale part of Houston. The business card will be a size 3.5 x 2 and the letterhead will be 8.5" x 11" with a standard #10 envelope.
I have uploaded a file with an idea that the dentist had for his cards. Please note that this is not the size that the card should be. It does provide the information required.
Updates
Thank you all for your submissions. They were each unique and special in their own way. My client has made a selection that he feels best meets his needs. I appreciate each of you taking the time to offer designs. Good luck to each of you...I hope to see you back in MarblePost on future projects.
Industry/Entity Type
Business
Look and feel
Each slider illustrates characteristics of the customer's brand and the style your logo design should communicate.

```html
<!DOCTYPE html>
<html lang="en">
<head>
<meta charset="utf-8">
<title>Brightwater Smile &amp; Restorative Care – #10 Envelope</title>
<link href="https://fonts.googleapis.com/css2?family=Open+Sans:wght@400;600&display=swap" rel="stylesheet">
<style>
  :root {
    --backdrop: #e4e4e4;
    --paper: #ffffff;
    --maroon: #8a3d44;
    --maroon-light: #a3686c;
    --maroon-deep: #7f3238;
    --shadow: rgba(0,0,0,0.16);
  }
  * { box-sizing: border-box; margin: 0; padding: 0; }
  html, body {
    width: 1200px; height: 1200px; overflow: hidden;
    background: var(--backdrop);
    font-family: "Open Sans", Arial, sans-serif;
    color: var(--maroon);
  }
  .envelope {
    position: absolute;
    left: 220px;
    width: 760px; height: 330px;
    background: var(--paper);
    box-shadow: 0 10px 24px var(--shadow);
  }
  .envelope--front { top: 110px; }
  .envelope--back { top: 650px; overflow: hidden; }

  /* Front: return-address block */
  .return-block {
    position: absolute; left: 34px; top: 196px;
  }
  .practice-name {
    display: flex; align-items: center; gap: 10px;
    font-weight: 600; font-size: 15px; line-height: 1.15;
    text-transform: uppercase; letter-spacing: 0.5px;
    color: var(--maroon);
  }
  .practice-name .mark {
    width: 22px; height: 22px; border-radius: 50%;
    background: var(--maroon); flex: none;
  }
  .practitioner {
    margin-top: 6px; font-size: 11.5px; font-weight: 600;
    color: var(--maroon); white-space: nowrap;
  }
  .practitioner .title { font-weight: 400; }
  .dotted-rule {
    width: 60px; border-top: 2px dotted var(--maroon);
  }
  .return-block .dotted-rule { margin: 4px 0 0 180px; }

  /* Back: flap and contact */
  .flap {
    position: absolute; left: 0; top: 0; width: 760px; height: 170px;
    background: linear-gradient(160deg, var(--maroon-deep) 0%, var(--maroon-light) 45%, var(--maroon-deep) 100%);
    border-radius: 0 0 28px 28px;
  }
  .contact {
    position: absolute; left: 0; right: 0; top: 238px;
    text-align: center; font-size: 9.5px; line-height: 1.6;
    color: var(--maroon);
  }
  .contact .dotted-rule { margin: 0 auto 2px; width: 70px; }
  .contact-row { display: flex; justify-content: center; gap: 14px; align-items: center; }
  .contact-item { display: inline-flex; align-items: center; gap: 4px; }
  .contact-item svg { width: 10px; height: 10px; fill: var(--maroon); }
</style>
</head>
<body>

<section class="envelope envelope--front" aria-label="Envelope front">
  <div class="return-block">
    <div class="practice-name">
      <span class="mark"></span>
      <span>Brightwater Smile &amp;<br>Restorative Care</span>
    </div>
    <p class="practitioner">Daniel Moreno, D.D.S., PLLC, <span class="title">Prosthodontist</span></p>
    <div class="dotted-rule"></div>
  </div>
</section>

<section class="envelope envelope--back" aria-label="Envelope back">
  <div class="flap"></div>
  <div class="contact">
    <div class="dotted-rule"></div>
    <p>18 Linden Park Road Suite 310 Riverton, OK 73071</p>
    <div class="contact-row">
      <span class="contact-item">
        <svg viewBox="0 0 10 10"><path d="M2 0h2l1 3-1.5 1a6 6 0 0 0 2.5 2.5L7 5l3 1v2c0 1-1 2-2 2A8 8 0 0 1 0 2c0-1 1-2 2-2z"/></svg>
        405-555-0142
      </span>
      <span class="contact-item">
        <svg viewBox="0 0 10 10"><rect x="1" y="3" width="8" height="6" rx="1"/><rect x="3" y="0" width="4" height="3"/></svg>
        405-555-0187
      </span>
      <span class="contact-item">
        <svg viewBox="0 0 10 10"><path d="M0 2h10v6H0z" fill="none" stroke="#8a3d44" stroke-width="1"/><path d="M0 2l5 4 5-4" fill="none" stroke="#8a3d44" stroke-width="1"/></svg>
        DrMoreno@brightwatercare.com
      </span>
    </div>
  </div>
</section>

</body>
</html>
```